Business Card

We need some ideas for corporate business cards. I'm interested in a double sided card, with one side featuring our corporate logo, the other side with employee information.

Corporate colors, logo etc. available at www.brivalo.com

Industry/Entity Type

Business

Requirements
Must have
• The "Brivalo" logo with stylized "O"

Nice to have
• Preferred font is calibri

```html
<!DOCTYPE html>
<html lang="en">
<head>
<meta charset="utf-8">
<title>Brivalo Business Card</title>
<link rel="stylesheet" href="https://fonts.googleapis.com/css2?family=Carlito:wght@400;700&display=swap">
<style>
  :root {
    --card-blue: #4a6491;
    --card-blue-deep: #3f5783;
    --ink-white: #ffffff;
    --page: #ffffff;
  }
  * { margin: 0; padding: 0; box-sizing: border-box; }
  html, body {
    width: 1200px;
    height: 1000px;
    overflow: hidden;
    background: var(--page);
    font-family: "Carlito", "Calibri", sans-serif;
  }
  .canvas {
    position: relative;
    width: 1200px;
    height: 1000px;
  }
  .card {
    position: absolute;
    width: 696px;
    height: 398px;
    background: var(--card-blue);
    color: var(--ink-white);
  }
  .card--front { left: 51px; top: 63px; }
  .card--back  { left: 439px; top: 509px; overflow: hidden; }

  .brand-name {
    position: absolute;
    left: 0;
    width: 100%;
    top: 152px;
    text-align: center;
    font-size: 84px;
    font-weight: 700;
    letter-spacing: 10px;
    line-height: 1;
    color: var(--ink-white);
  }

  .circuit-backdrop {
    position: absolute;
    inset: 0;
    background: linear-gradient(135deg, var(--card-blue) 0%, var(--card-blue-deep) 50%, var(--card-blue) 100%);
  }

  .employee {
    position: absolute;
    left: 220px;
    top: 78px;
    width: 300px;
  }
  .employee__name {
    font-size: 46px;
    font-weight: 700;
    line-height: 1;
    white-space: nowrap;
  }
  .employee__title {
    margin-top: 10px;
    margin-left: 18px;
    font-size: 22px;
    font-weight: 700;
    line-height: 1;
    white-space: nowrap;
  }
  .employee__rule {
    margin-top: 11px;
    margin-left: 18px;
    width: 232px;
    height: 2px;
    background: var(--ink-white);
  }

  .contact {
    position: absolute;
    left: 214px;
    display: flex;
    align-items: center;
    gap: 9px;
    font-size: 20px;
    font-weight: 700;
    white-space: nowrap;
  }
  .contact--email { top: 235px; }
  .contact--phone { top: 285px; }
  .contact__icon { width: 38px; height: 38px; flex: none; }
</style>
</head>
<body>
<main class="canvas">
  <section class="card card--front" aria-label="Card front">
    <div class="brand-name">BRIVALO</div>
  </section>

  <section class="card card--back" aria-label="Card back">
    <div class="circuit-backdrop" role="img" aria-label="Faint circuit-board pattern of traces and pads in muted blue, mauve and tan tones"></div>

    <div class="employee">
      <div class="employee__name">Name Here</div>
      <div class="employee__title">Chief Executive Officer</div>
      <div class="employee__rule"></div>
    </div>

    <div class="contact contact--email">
      <svg class="contact__icon" viewBox="0 0 38 38" aria-hidden="true">
        <circle cx="19" cy="19" r="17" fill="none" stroke="#fff" stroke-width="2"/>
        <path d="M10 16 L19 10 L28 16 V27 H10 Z" fill="none" stroke="#fff" stroke-width="2" stroke-linejoin="round"/>
        <path d="M10 16 L19 22 L28 16" fill="none" stroke="#fff" stroke-width="2" stroke-linejoin="round"/>
      </svg>
      <span>namehere@brivalo.com</span>
    </div>

    <div class="contact contact--phone">
      <svg class="contact__icon" viewBox="0 0 38 38" aria-hidden="true">
        <circle cx="19" cy="19" r="17" fill="none" stroke="#fff" stroke-width="2"/>
        <path d="M13 10 l4 0 l2 6 l-3 2 c1.5 3 3 4.5 6 6 l2 -3 l6 2 l0 4 c0 1 -1 2 -2 2 c-9 -1 -15 -7 -16 -16 c0 -1 1 -2 1 -3 z" fill="#fff"/>
      </svg>
      <span>number here</span>
    </div>
  </section>
</main>
</body>
</html>
```